Brochure Annual Report Design

I want to create a brochure / annual report for our company. Can you help me. I like this design. https://plumvaultdesigns.net/Zorvik/4829175-Annual-Report-2018. Here is our company website www.brimdental.com. Please take the logo from there. Our website needs an upgrade in how it looks. I would like the brochure annual report and the website to look somewhat congruent. I also want to create a very high end magazine that is fun for our company eventually.

We are a company that helps dentists create better practices by really improving the way they do business and motivating their teams. As a result they have more fun, more profit, happier team members, and they all have better lives.

Target Market(s)

dentist

Industry/Entity Type

Dental

Number of Pages Required

5+ page

Colors
0255a3
85cae6
ffffff

Requirements
Must have
• Must look really good.
Nice to have
• Any creative suggestions are welcomed. I need a website that looks congruent to the brochure and annual report. I also want to create a very high end magazine that is fun for our company eventually.
Should not have
• I don't like low quality design.

```html
<!DOCTYPE html>
<html lang="en">
<head>
<meta charset="utf-8">
<title>Brim Dental — Annual Report 2018</title>
<link href="https://fonts.googleapis.com/css2?family=Poppins:wght@300;400;500;600;700;800&family=Lato:wght@400;700&display=swap" rel="stylesheet">
<style>
  :root{
    --blue:#1d6fb8;
    --blue-light:#7ba7d3;
    --ink:#333a40;
    --muted:#6b7178;
    --bar:#e4e5e7;
    --page:#ffffff;
    --backdrop:#e3dcd7;
  }
  *{box-sizing:border-box;margin:0;padding:0}
  html,body{width:1200px;height:1200px;overflow:hidden;background:var(--backdrop)}
  body{position:relative;font-family:'Lato',sans-serif;color:var(--ink)}
  .spread{position:absolute;left:220px;width:760px;height:537px;background:var(--page);box-shadow:0 6px 18px rgba(60,40,30,.18)}
  .spread--cover{top:30px}
  .spread--inner{top:633px}
  .spread svg.art{position:absolute;inset:0;width:760px;height:537px}
  .spine{position:absolute;left:379px;top:0;width:2px;height:537px;background:linear-gradient(90deg,rgba(0,0,0,.06),rgba(0,0,0,0))}
  .abs{position:absolute}

  .brand{font-family:'Poppins',sans-serif;font-weight:600;color:var(--blue);letter-spacing:.2px}
  .brand--back{left:24px;top:392px;font-size:30px}
  .brand--front{right:18px;top:10px;font-size:22px}
  .brand-name{left:26px;top:436px;font-family:'Poppins',sans-serif;font-weight:700;font-size:9.5px;color:var(--blue);letter-spacing:.8px}
  .contact{left:26px;top:454px;font-size:7.5px;color:var(--muted);line-height:11px;list-style:none}
  .contact li{display:flex;align-items:flex-start;gap:5px}
  .contact svg{width:7px;height:7px;margin-top:2px;flex:none}
  .cover-site{left:410px;top:488px;font-size:8px;letter-spacing:1.4px;color:var(--muted);display:flex;align-items:center;gap:5px}
  .cover-site i{width:5px;height:5px;border-radius:50%;background:var(--blue);display:block}

  .title{font-family:'Poppins',sans-serif;text-align:right;right:22px;top:160px;line-height:1}
  .title .annual{display:block;font-weight:300;font-size:27px;color:var(--ink)}
  .title .report{display:block;font-weight:500;font-size:36px;color:var(--blue);margin-top:2px}
  .title .year{display:block;font-weight:700;font-size:36px;color:var(--ink);margin-top:2px}

  .welcome{left:26px;top:222px;font-family:'Poppins',sans-serif;line-height:1}
  .welcome .big{display:block;font-weight:800;font-size:33px;color:var(--blue)}
  .welcome .sub{display:block;font-weight:400;font-size:15px;color:var(--ink);margin-top:2px}
  .welcome .accent{display:block;font-weight:700;font-size:24px;color:var(--blue-light);margin-top:2px}
  .body-copy{left:26px;top:318px;width:330px;font-size:7.6px;line-height:10px;color:var(--ink)}
  .body-copy p+p{margin-top:9px}

  .toc{left:400px;top:0;width:360px;height:537px}
  .toc-head{position:absolute;left:30px;top:40px;font-family:'Poppins',sans-serif;font-size:24px;font-weight:700;color:var(--ink)}
  .toc-head span{color:var(--blue)}
  .toc-rule{position:absolute;left:30px;top:78px;width:310px;height:1.5px;background:var(--blue-light)}
  .toc-lede{position:absolute;left:30px;top:84px;font-size:7.5px;color:var(--muted)}
  .toc-list{position:absolute;left:30px;top:104px;width:310px;list-style:none}
  .toc-list li{display:flex;justify-content:space-between;align-items:center;height:26px}
  .toc-item{background:var(--bar);height:17px;width:190px;font-size:7.8px;line-height:17px;padding-left:6px;color:var(--ink)}
  .toc-page{width:48px;height:20px;line-height:20px;text-align:center;font-size:9px;color:#fff;background:var(--blue);font-family:'Poppins',sans-serif}
  .toc-list li:nth-child(even) .toc-page{background:var(--blue-light)}
</style>
</head>
<body>

<section class="spread spread--cover" aria-label="Cover spread">
  <svg class="art" viewBox="0 0 760 537" aria-hidden="false">
    <defs>
      <linearGradient id="toothPhoto" x1="0" y1="0" x2="1" y2="1">
        <stop offset="0" stop-color="#d7e0ea"/><stop offset=".6" stop-color="#eef2f7"/><stop offset="1" stop-color="#c9d6e6"/>
      </linearGradient>
      <linearGradient id="clinicPhoto" x1="0" y1="0" x2="1" y2="1">
        <stop offset="0" stop-color="#c2d3e4"/><stop offset=".5" stop-color="#e3e9f0"/><stop offset="1" stop-color="#a9c2db"/>
      </linearGradient>
      <linearGradient id="greyPanel" x1="0" y1="0" x2="1" y2="1">
        <stop offset="0" stop-color="#f3f3f4"/><stop offset="1" stop-color="#dcdde0"/>
      </linearGradient>
    </defs>
    <!-- back cover -->
    <path role="img" aria-label="Photo: hand holding a dental model and mirror" d="M0,112 L120,70 L380,44 L380,248 Q260,262 150,272 L0,272 Z" fill="url(#toothPhoto)"/>
    <polygon points="0,80 122,36 122,68 0,112" fill="var(--blue-light)"/>
    <polygon points="122,36 380,10 380,44 122,68" fill="var(--blue)"/>
    <path d="M150,284 Q270,274 380,256" fill="none" stroke="var(--blue)" stroke-width="6"/>
    <!-- front cover -->
    <path role="img" aria-label="Photo: dentists treating a patient" d="M380,44 L610,112 L640,100 L560,200 Q480,250 380,262 Z" fill="url(#clinicPhoto)"/>
    <path d="M640,100 L760,58 L760,300 L500,300 Q560,260 640,100 Z" fill="url(#greyPanel)"/>
    <polygon points="380,10 610,78 610,112 380,44" fill="var(--blue)"/>
    <polygon points="610,78 760,26 760,58 610,112" fill="var(--blue-light)"/>
    <path d="M380,270 Q490,258 570,206" fill="none" stroke="var(--blue)" stroke-width="5"/>
    <polygon points="566,312 668,312 648,364" fill="var(--blue)"/>
  </svg>
  <div class="spine"></div>

  <div class="abs brand brand--back">Brim Dental</div>
  <div class="abs brand-name">BRIM DENTAL</div>
  <ul class="abs contact">
    <li><svg viewBox="0 0 10 10"><path d="M2 1l2 2-1 1.5a6 6 0 0 0 2.5 2.5L7 6l2 2-1.5 1.5C4 9 1 6 .5 2.5z" fill="var(--blue)"/></svg>800.555.0142</li>
    <li><svg viewBox="0 0 10 10"><circle cx="5" cy="5" r="4" fill="none" stroke="var(--blue)" stroke-width="1.4"/></svg>www.brimdental.com</li>
    <li><svg viewBox="0 0 10 10"><path d="M5 0a3.5 3.5 0 0 1 3.5 3.5C8.5 6 5 10 5 10S1.5 6 1.5 3.5A3.5 3.5 0 0 1 5 0z" fill="var(--blue)"/></svg>4410 Larkspur Avenue<br>Suite 210 Fenwick, KS 66099</li>
  </ul>

  <div class="abs brand brand--front">Brim Dental</div>
  <h1 class="abs title"><span class="annual">Annual</span><span class="report">REPORT</span><span class="year">2018</span></h1>
  <div class="abs cover-site"><i></i>www.brimdental.com</div>
</section>

<section class="spread spread--inner" aria-label="Welcome and contents spread">
  <svg class="art" viewBox="0 0 760 537">
    <defs>
      <linearGradient id="smilePhoto" x1="0" y1="0" x2="1" y2="0">
        <stop offset="0" stop-color="#c99a84"/><stop offset=".45" stop-color="#e6cfc3"/><stop offset="1" stop-color="#e9edf2"/>
      </linearGradient>
    </defs>
    <path role="img" aria-label="Photo: smiling woman" d="M22,58 L128,30 L250,175 L22,205 Z" fill="url(#smilePhoto)"/>
    <polygon points="118,0 196,0 300,158 246,176" fill="var(--blue)"/>
    <polygon points="246,176 300,158 380,128 380,178 280,206" fill="var(--blue-light)"/>
    <path d="M230,218 Q310,200 380,182 L380,246 Q330,218 230,218 Z" fill="var(--blue)"/>
  </svg>
  <div class="spine"></div>

  <h2 class="abs welcome"><span class="big">WELCOME</span><span class="sub">TO OUR YEARLY</span><span class="accent">Annual REPORT</span></h2>
  <div class="abs body-copy">
    <p>Lorem Ipsum is simply dummy text of the printing and typesetting industry. Lorem Ipsum has been the industry's standard dummy text ever since the 1500s, when an unknown printer took a galley of type and scrambled it to make a type specimen book. It has survived not only five centuries, but also the leap into electronic typesetting, remaining essentially unchanged. It was popularised in the 1960s with the release of Letraset sheets containing Lorem Ipsum passages, and more recently with desktop publishing software like Aldus PageMaker including versions of Lorem Ipsum.</p>
    <p>Lorem Ipsum is simply dummy text of the printing and typesetting industry. Lorem Ipsum has been the industry's standard dummy text ever since the 1500s, when an unknown printer took a galley of type and scrambled it to make a type specimen book. It has survived not only five centuries, but also the leap into electronic typesetting, remaining essentially unchanged. It was popularised in the 1960s with the release of Letraset sheets containing Lorem Ipsum passages, and more recently with desktop publishing software like Aldus PageMaker including versions of Lorem Ipsum.</p>
  </div>

  <div class="abs toc">
    <h2 class="toc-head">Table Of <span>CONTENTS</span></h2>
    <div class="toc-rule"></div>
    <p class="toc-lede">Lorem Ipsum is simply dummy text of the printing and typesetting industry</p>
    <ol class="toc-list">
      <li><span class="toc-item">Lorem Ipsum is simply dummy text</span><span class="toc-page">00</span></li>
      <li><span class="toc-item">Lorem Ipsum is simply dummy text</span><span class="toc-page">00</span></li>
      <li><span class="toc-item">Lorem Ipsum is simply dummy text</span><span class="toc-page">00</span></li>
      <li><span class="toc-item">Lorem Ipsum is simply dummy text</span><span class="toc-page">00</span></li>
      <li><span class="toc-item">Lorem Ipsum is simply dummy text</span><span class="toc-page">00</span></li>
      <li><span class="toc-item">Lorem Ipsum is simply dummy text</span><span class="toc-page">00</span></li>
      <li><span class="toc-item">Lorem Ipsum is simply dummy text</span><span class="toc-page">00</span></li>
      <li><span class="toc-item">Lorem Ipsum is simply dummy text</span><span class="toc-page">00</span></li>
      <li><span class="toc-item">Lorem Ipsum is simply dummy text</span><span class="toc-page">00</span></li>
      <li><span class="toc-item">Lorem Ipsum is simply dummy text</span><span class="toc-page">00</span></li>
      <li><span class="toc-item">Lorem Ipsum is simply dummy text</span><span class="toc-page">00</span></li>
      <li><span class="toc-item">Lorem Ipsum is simply dummy text</span><span class="toc-page">00</span></li>
      <li><span class="toc-item">Lorem Ipsum is simply dummy text</span><span class="toc-page">00</span></li>
      <li><span class="toc-item">Lorem Ipsum is simply dummy text</span><span class="toc-page">00</span></li>
      <li><span class="toc-item">Lorem Ipsum is simply dummy text</span><span class="toc-page">00</span></li>
    </ol>
  </div>
</section>

</body>
</html>
```